Tervane Electronic Security Web Site

We need a web site for our new company based in Sydney Australia.
We specialize in consulting supplying and installing electronic security systems. These include CCTV, Access control, Alarms, Intercom and Network cabling.
We pride our selves in giving our customers peace of mind giving back security and freedom to our customers. We pride in customer service quality products and expertise with and we do the job as though it is for our personal friends and family.
We need to be able to edit web site contents and update information.

```html
<!DOCTYPE html>
<html lang="en">
<head>
<meta charset="utf-8">
<title>Tervane Electronic Security</title>
<link href="https://fonts.googleapis.com/css2?family=Questrial&family=Open+Sans:wght@400;600&display=swap" rel="stylesheet">
<style>
:root{
  --brand:#1a7fa8;
  --brand-dark:#0e3f5c;
  --nav-top:#2a7fae;
  --nav-bottom:#15577e;
  --caption:#29b6dc;
  --ink:#1f2a33;
  --muted:#6b7780;
  --link:#1a7fa8;
  --line:#dfe6ec;
  --footer:#164f72;
}
*{margin:0;padding:0;box-sizing:border-box}
html,body{width:896px;height:1200px;overflow:hidden;background:#fff}
body{position:relative;font-family:"Open Sans",sans-serif;color:var(--ink)}
.abs{position:absolute}
.head-font{font-family:"Questrial",sans-serif}

.logo{left:94px;top:30px;font-family:"Questrial",sans-serif;font-size:27px;color:var(--brand)}
.call{right:90px;top:32px;text-align:right;font-family:"Questrial",sans-serif}
.call-label{font-size:11px;color:var(--brand)}
.call-number{font-size:16px;color:var(--brand-dark);display:flex;align-items:center;gap:5px;margin-top:2px}

.nav{left:0;top:78px;width:896px;height:36px;background:linear-gradient(var(--nav-top),var(--nav-bottom))}
.nav ul{list-style:none;display:flex;position:absolute;left:94px;top:0;height:36px}
.nav li{height:36px;line-height:36px;text-align:center;font-family:"Questrial",sans-serif;font-size:11.5px;color:#fff;border-right:1px solid rgba(0,0,0,.22)}
.nav li:last-child{border-right:none}

.hero{left:0;top:114px;width:896px;height:364px;background:linear-gradient(100deg,#d9d2cb 0%,#c9b7a8 45%,#3a3a3a 62%,#b99a80 80%,#d8c2ae 100%)}
.caption{left:94px;top:240px;width:308px;height:118px;background:var(--caption);opacity:.95;border-radius:2px;padding:20px 26px;color:#fff}
.caption-kicker{font-family:"Questrial",sans-serif;font-size:14.5px}
.caption-title{font-family:"Questrial",sans-serif;font-size:23px;margin-top:2px}
.caption-text{font-size:8px;line-height:13px;margin-top:6px;opacity:.95}
.dots{left:424px;top:436px;display:flex;gap:4px}
.dots span{width:9.5px;height:9.5px;border-radius:50%;background:#fff}

.band{left:0;top:478px;width:896px;height:130px;background:linear-gradient(#ececec,#fff)}
.service-panel{left:76px;top:457px;width:744px;height:170px;background:#fff}
.service{top:472px;width:172px;height:141px;border:1px solid var(--line);background:linear-gradient(#fff,#f2f6f9)}
.service-photo{height:94px}
.service-title{font-family:"Questrial",sans-serif;font-size:14px;color:var(--brand);padding:9px 0 0 13px}
.service-sub{font-size:8.5px;color:var(--muted);padding:2px 0 0 13px}

.about-title{left:90px;top:662px;font-family:"Questrial",sans-serif;font-size:21.5px;color:var(--ink)}
.about-text{left:92px;top:698px;width:440px;font-size:8.6px;line-height:15.3px;color:var(--muted)}
.about-text p+p{margin-top:3px}
.video{left:560px;top:660px;width:249px;height:158px;background:#fff;border:1px solid var(--line);box-shadow:0 1px 3px rgba(0,0,0,.2);padding:4px}
.video-still{width:100%;height:100%;background:linear-gradient(135deg,#e6e9ee 0%,#c9ced8 50%,#8a7a60 80%,#2a2a2a 100%);position:relative}
.play{position:absolute;left:104px;top:50px}

.blog-title{left:90px;top:850px;font-family:"Questrial",sans-serif;font-size:18px;color:var(--brand)}
.post{top:886px;width:224px}
.post-photo{height:97px}
.post-title{font-family:"Questrial",sans-serif;font-size:13px;color:var(--ink);margin-top:10px}
.post-text{font-size:8.6px;line-height:15px;color:var(--muted);margin-top:4px}
.post-more{font-size:9px;font-weight:600;color:var(--link);margin-top:4px}

.footer{left:0;top:1106px;width:896px;height:94px;background:var(--footer)}
.footer-links{left:90px;top:1127px;font-family:"Questrial",sans-serif;font-size:10.5px;color:#fff;word-spacing:1px}
.footer-copy{left:90px;top:1153px;font-size:8.6px;color:#d6e4ee}
.social{left:711px;top:1129px;display:flex;gap:3px}
.social span{width:19px;height:19px;border-radius:50%;background:#fff}
</style>
</head>
<body>

<div class="abs logo">Tervane Electronic Security</div>
<div class="abs call">
  <div class="call-label">24/7 Call Now</div>
  <div class="call-number">
    <svg width="17" height="17" viewBox="0 0 20 20" aria-hidden="true"><circle cx="10" cy="10" r="8.8" fill="none" stroke="#1a7fa8" stroke-width="1.4"/><path d="M7 5.5c-.8.4-1.2 1.2-1 2.2.5 2.6 2.6 5.1 5.2 6 .9.3 1.8 0 2.3-.8l-1.6-1.6-1.2.6c-1-.5-2-1.5-2.5-2.6l.6-1.2L7 5.5z" fill="#1a7fa8"/></svg>
    02-5550 184 732
  </div>
</div>

<nav class="abs nav">
  <ul>
    <li style="width:72px">HOME</li>
    <li style="width:91px">ABOUT US</li>
    <li style="width:88px">SERVICES</li>
    <li style="width:78px">HIRE US</li>
    <li style="width:98px">PRODUCTS</li>
    <li style="width:115px">TESTIMONIALS</li>
    <li style="width:74px">VIDEO</li>
    <li style="width:91px">CONTACT</li>
  </ul>
</nav>

<div class="abs hero" role="img" aria-label="Technician in gloves installing a security camera under a house eave"></div>
<div class="abs caption">
  <div class="caption-kicker">Mauris vel lacus vitae vestibulum</div>
  <div class="caption-title">Intalling Security System</div>
  <div class="caption-text">Integer orci tellus tristique vitae consequat nec porta vel lectus Nulla sit amet diam Duis non nunc</div>
</div>
<div class="abs dots"><span></span><span></span><span></span><span></span></div>

<div class="abs band"></div>
<div class="abs service-panel"></div>
<div class="abs service" style="left:90px">
  <div class="service-photo" role="img" aria-label="CCTV camera mounted on a wooden wall" style="background:linear-gradient(135deg,#c98a4e,#e8e4df 50%,#a8652f)"></div>
  <div class="service-title">CCTV System</div>
  <div class="service-sub">Morbi diam mauris viverra gravida</div>
</div>
<div class="abs service" style="left:271px">
  <div class="service-photo" role="img" aria-label="Fingerprint access control keypad beside a glass door" style="background:linear-gradient(90deg,#7f9190,#b9c6c4 40%,#3b3f40 70%,#8a7460)"></div>
  <div class="service-title">Access Control</div>
  <div class="service-sub">Morbi diam mauris viverra gravida</div>
</div>
<div class="abs service" style="left:451px">
  <div class="service-photo" role="img" aria-label="Intruder at a window being caught by a security system" style="background:linear-gradient(90deg,#c9cfcf,#6f7d78 45%,#9aa597 70%,#c8d2c4)"></div>
  <div class="service-title">Security System</div>
  <div class="service-sub">Morbi diam mauris viverra gravida</div>
</div>
<div class="abs service" style="left:632px">
  <div class="service-photo" role="img" aria-label="Network patch panel with cables" style="background:linear-gradient(135deg,#5d6f9a,#c8d0e4 50%,#7d8db5)"></div>
  <div class="service-title">Network Cabling</div>
  <div class="service-sub">Morbi diam mauris viverra gravida</div>
</div>

<h1 class="abs about-title">Little About Our Company</h1>
<div class="abs about-text">
  <p>Etiam est nunc venenatis in tristique eu imperdiet ac nisl Cum sociis natoque penatibus et magnis dis parturient montes nascetur ridiculus mus In iaculis facilisis massa Etiam eu urna Sed porta Suspendisse quam leo molestie sed luctus quis feugiat in pede Fusce tellus Sed metus augue convallis et vehicula ut pulvinar eu ante Integer orci tellus tristique vitae consequat nec porta vel lectus</p>
  <p>Vivamus porttitor purus nisi eleifend libero a tempus libero lectus feugiat felis Morbi diam mauris viverra in gravida eu mattis in ante Morbi eget arcu Morbi porta libero id ullamcorper</p>
</div>
<div class="abs video">
  <div class="video-still" role="img" aria-label="Hand turning a key on an alarm control panel">
    <svg class="play" width="36" height="36" viewBox="0 0 36 36" aria-hidden="true"><circle cx="18" cy="18" r="18" fill="#fff"/><path d="M14 11l11 7-11 7z" fill="#111"/></svg>
  </div>
</div>

<h2 class="abs blog-title">Latest Projects &amp; Blog</h2>
<div class="abs post" style="left:90px">
  <div class="post-photo" role="img" aria-label="Dome camera on the ceiling of an office corridor" style="background:linear-gradient(90deg,#8d8a80,#d8d6cf 50%,#e9e7e2)"></div>
  <div class="post-title">Etiam est nunc venenatis</div>
  <div class="post-text">Cum sociis natoque penatibus et magnis dis partu-<br>rient montes nascetur ridiculus mus consequat</div>
  <div class="post-more">Read More</div>
</div>
<div class="abs post" style="left:333px">
  <div class="post-photo" role="img" aria-label="Woman swiping an access card at a glass door" style="background:linear-gradient(90deg,#2d3a44,#b9c8d0 45%,#5f7788 80%,#26343e)"></div>
  <div class="post-title">Vivamus porttitor puru</div>
  <div class="post-text">Cum sociis natoque penatibus et magnis dis partu-<br>rient montes nascetur ridiculus mus consequat</div>
  <div class="post-more">Read More</div>
</div>
<div class="abs post" style="left:574px">
  <div class="post-photo" role="img" aria-label="Finger pressing an alarm keypad" style="background:linear-gradient(90deg,#e6ebf1,#c4cfdd 60%,#b7c2d1)"></div>
  <div class="post-title">Curabitur iaculis tempus</div>
  <div class="post-text">Cum sociis natoque penatibus et magnis dis partu-<br>rient montes nascetur ridiculus mus consequat</div>
  <div class="post-more">Read More</div>
</div>

<footer class="abs footer"></footer>
<div class="abs footer-links">HOME &nbsp;|&nbsp; ABOUT US &nbsp;|&nbsp; SERVICES &nbsp;|&nbsp; HIRE US &nbsp;|&nbsp; PRODUCTS &nbsp;|&nbsp; TESTIMONIALS &nbsp;|&nbsp; VIDEO &nbsp;|&nbsp; CONTACT</div>
<div class="abs footer-copy">© 2014 Company Name &nbsp;All right reserved &nbsp;Term of Use</div>
<div class="abs social" aria-label="Social links"><span></span><span></span><span></span><span></span></div>

</body>
</html>
```